Groundbreaking Automotive Product launch

Create a package insert for sample packs to be given away at industry trade show. The new product is an innovative automotive bumper protection system that is being introduced at a major trade show.

Fendrashield (www.fendrashield.biz) is a peel and stick clear film system that protects automobile bumpers from nicks, scratches, scrapes and scuffs. Our company is planning to sell the product to owners / operators of automated car wash businesses who will apply the product to car bumpers at the end of their normal wash cycle.

This package insert will be for sample packs that we will give away to car wash owners / operators at our trade show booth to encourage them to try the system on their own. The sample package (not for resale) includes 3 Fendrashield in a roll that is one inch in diameter and 5 inches high, one squeegee applicator (3 inch x 4 inch), and one 2 ounce bottle of spray lubricant ( 1 1/4 inch in diameter x 5 inches high). These contents will be contained in a clear plastic clamshell package. The insert is approximately 4 inches wide by 6 inches tall.

The face of the insert will not be obstructed by the package contents. it needs to contain the product logo (we will provide) and some attractive artwork showing the product in place on a car bumper - this needs to illustrate that the product is virtually invisible (except perhaps for a sparkle of sunlight off its highly polished surface) and does not change the appearance of the vehicle. The face of the insert will also require text indicating that product application helps them differentiate their car wash from the competition, is quick and easy without capital expense or staff training, can be done in a matter of seconds without disrupting the normal car wash process, preserves the appearance and resale value of the owner's vehicle, that the product is removable, the product is engineered to last up to one year, and that providing this bumper protection system can dramatically increase profits per transaction. Finally, our company contact information will also need to be included.

the back of the package insert will be obstructed partially by package contents but that does not affect insert design. the back of the insert merely needs to print application instructions (in black and white) which we will provide.
Updates

Project Deadline Extended

Target Market(s)

Owners / operators of automated car wash businesses located primarily in metropolitan areas.

Industry/Entity Type

Automotive

Requirements
Must have
• artwork must clearly indicate the product is applied to the flat surface of an automobile bumper while at the same time prominently featuring the product logo (we actually do print the logo design in one corner of the product itself).
Nice to have
• artwork that indicates the product is crystal clear and enhances the shine of the vehicle paint.
Should not have
• artwork should not suggest product is applied to bumper sections with dramatic or complex curves

```html
<!DOCTYPE html>
<html lang="en">
<head>
<meta charset="utf-8">
<title>Installing Method</title>
<link href="https://fonts.googleapis.com/css2?family=Open+Sans:wght@400;600;700;800&display=swap" rel="stylesheet">
<style>
  :root {
    --page-bg: #ececec;
    --title-band: #dcdcdc;
    --title-ink: #5a5a5a;
    --panel: #34475a;
    --panel-head: #2c3d4e;
    --panel-rule: #5d7186;
    --badge: #f2a33a;
    --badge-ink: #ffffff;
    --text-light: #e6ebf0;
    --car-white: #f6f6f6;
    --car-grey: #d9dcdf;
    --bumper-shadow: #55595e;
    --frame: #d3d6d9;
  }
  * { box-sizing: border-box; margin: 0; padding: 0; }
  html, body { width: 800px; height: 1200px; overflow: hidden; }
  body {
    background: var(--page-bg);
    font-family: "Open Sans", Arial, sans-serif;
    position: relative;
  }
  .page-title {
    height: 108px;
    background: var(--title-band);
    display: flex;
    align-items: center;
    justify-content: center;
    color: var(--title-ink);
    font-weight: 800;
    font-size: 66px;
    letter-spacing: -0.5px;
  }
  .steps {
    position: absolute;
    top: 134px;
    left: 34px;
    right: 34px;
    display: flex;
    flex-direction: column;
    gap: 36px;
  }
  .step {
    height: 306px;
    display: flex;
  }
  .step-art {
    width: 366px;
    flex: none;
    border-radius: 10px 0 0 10px;
    border: 3px solid var(--frame);
    background:
      radial-gradient(ellipse 40% 18% at 30% 88%, rgba(60,64,70,0.55), rgba(60,64,70,0) 100%),
      linear-gradient(180deg,
        var(--car-white) 0%,
        var(--car-grey) 22%,
        var(--car-white) 34%,
        var(--car-white) 58%,
        var(--car-grey) 68%,
        #9ca0a5 78%,
        var(--bumper-shadow) 86%,
        #8e9297 93%,
        var(--car-grey) 100%);
  }
  .step-panel {
    flex: 1;
    background: var(--panel);
    color: var(--text-light);
    display: flex;
    flex-direction: column;
  }
  .step-head {
    display: flex;
    align-items: center;
    gap: 16px;
    padding: 18px 18px 16px 20px;
    min-height: 98px;
    background: var(--panel-head);
    border-bottom: 2px solid var(--panel-rule);
  }
  .step-badge {
    width: 62px;
    height: 62px;
    background: var(--badge);
    color: var(--badge-ink);
    display: flex;
    align-items: center;
    justify-content: center;
    gap: 4px;
    flex: none;
  }
  .step-badge .label {
    writing-mode: vertical-rl;
    transform: rotate(180deg);
    font-size: 9px;
    font-weight: 700;
    letter-spacing: 1px;
  }
  .step-badge .num {
    font-size: 44px;
    font-weight: 400;
    line-height: 1;
  }
  .step-title {
    font-size: 17px;
    line-height: 1.4;
    font-weight: 700;
    color: #ffffff;
    text-transform: uppercase;
    letter-spacing: 0.3px;
  }
  .step-body {
    padding: 18px 24px;
    font-size: 15px;
    line-height: 1.6;
  }
</style>
</head>
<body>
  <h1 class="page-title">Installing Method</h1>

  <main class="steps">
    <section class="step">
      <div class="step-art" role="img" aria-label="Rear view of a white car with a hand wiping the bumper clean with a red cloth"></div>
      <div class="step-panel">
        <div class="step-head">
          <div class="step-badge"><span class="label">STEP</span><span class="num">1</span></div>
          <h2 class="step-title">Clean the bumper</h2>
        </div>
        <p class="step-body">Clean the bumper with any car wash soap and water.</p>
      </div>
    </section>

    <section class="step">
      <div class="step-art" role="img" aria-label="Rear view of a white car with a spray bottle misting soap solution onto the bumper"></div>
      <div class="step-panel">
        <div class="step-head">
          <div class="step-badge"><span class="label">STEP</span><span class="num">2</span></div>
          <h2 class="step-title">Spray the correct<br>film sticker</h2>
        </div>
        <p class="step-body">Select the correct size film sticker for your application, peel it from the backing paper, and spray the side to be placed onto the bumper with any dilute mild soap solution (such as Lumina dishwashing soap.)</p>
      </div>
    </section>

    <section class="step">
      <div class="step-art" role="img" aria-label="Rear view of a white car with a squeegee smoothing the clear film onto the bumper"></div>
      <div class="step-panel">
        <div class="step-head">
          <div class="step-badge"><span class="label">STEP</span><span class="num">3</span></div>
          <h2 class="step-title">Place the film sticker</h2>
        </div>
        <p class="step-body">Place the film sticker onto the bumper in the desired location. Starting from the middle and moving outward, use the pedded side of the squeegee to smooth out all wrinkles and bubbles.</p>
      </div>
    </section>
  </main>
</body>
</html>
```